Child sleep consultant needs a flyer to attract new clients

We need a flyer that will attract the attention of parents with children between newborn and 3 years old who may be experiencing sleep issues. The flyer will be placed at places such as community centres, doctors room, play centres, etc.

Our business is called Hushwood Nestlings and provides a sleep consultancy service. Our service essentially provides a routine for parents to follow and general advice. Our service is not medical advice.

We need the flyer to have an overall tone that is soft and peaceful however can catch the attention of parents who may be struggling on minimal sleep. We would like photos with minimal text. The colour we use is green.

We will provide the text to appear in the flyer once we have a better idea of the layout that we prefer for the flyer. The text however wont be extensive, just some catchy points.

We want to direct people to our website which is hushwoodnestlings.com.au. We also have a facebook page, which is Hushwood Nestlings.

We have a logo that we would like to appear on the flyer. We will attach the file once the uploader on pixel bazaar is fixed.

Our consultant is a certified Dream Anchor consultant, which has a separate logo that should appear somewhere on the logo. I will attach this once the uploader is fixed.

When we print the flyer - we want to print A5 SIZE ... please make sure the formatting is OK for this size.

Target Market(s)

Mums and Dads with children between newborn and 3 years old.

Industry/Entity Type

Consultant

Colors
cadf82

Requirements
Must have
• - Our logo.
• - Dream Anchor consultant logo - both attached to this brief.
• - Contact details - including phone number, email address and website
• - MUST be suitable for A5 printable size, double sided please.
• Must have the following text:
• If your baby or toddler isn't sleeping through the night, neither are you - and this means you are probably feeling physically and mentally exhausted, stressed, depressed and irritable, afraid you might be damaging your child and disconnected from your partner.
• The good news is nearly all healthy children 3 months or older are physically capable of sleeping 12 solid hours without waking. They just need to be taught the healthy sleep habits that enable them to do so.
• I can help with the sleep issues your child is experiencing. As a certified Dream Anchor (insert trademark TM here) I can help if:
• - your child will only fall asleep when nursing or bottle feeding
• - your child needs a dummy in order fall asleep
• - you're waking up with your child one or more times per night
• - your child needs to be rocked, patted, or taken for a car ride to go to sleep
• - your own lack of sleep is starting to take a toll on your family
• I've been personally trained by Marla Penwick, best selling author of the Dream Anchor (insert trade mark symbol here) Program to teach her sleep training methods to families like yours. Marla's methods have already helped over 30,000 parents and children and I'd be delighted to help your family next!
• Call or email for a free 15 minute consultation
• I would love to connect with you to talk about your child's specific situation and discuss different solutions.

```html
<!DOCTYPE html>
<html lang="en">
<head>
<meta charset="utf-8">
<title>Hushwood Nestlings – Sleep Consultancy Flyer</title>
<link rel="stylesheet" href="https://fonts.googleapis.com/css2?family=Open+Sans:wght@400;600;700;800&display=swap">
<style>
:root{
  --green:#cadf82;
  --green-deep:#9dbd3e;
  --green-text:#7fa326;
  --ink:#4a4a4a;
  --ink-soft:#6b6b6b;
  --paper:#ffffff;
  --backdrop:#dcdcdd;
  --photo-grey-a:#9a9a9a;
  --photo-grey-b:#e2e2e2;
  --photo-warm-a:#d8c4b8;
  --photo-warm-b:#5c6070;
}
*{box-sizing:border-box;margin:0;padding:0}
html,body{width:1200px;height:800px;overflow:hidden}
body{background:var(--backdrop);font-family:"Open Sans",Arial,sans-serif;color:var(--ink);position:relative}
.flyer{position:absolute;top:60px;width:480px;height:680px;background:var(--paper);overflow:hidden;box-shadow:0 10px 30px rgba(0,0,0,.25)}
.flyer--front{left:90px}
.flyer--back{left:630px}
.flyer svg.shapes{position:absolute;inset:0}
.brand{position:absolute;display:flex;align-items:center;gap:8px}
.brand__dot{width:28px;height:28px;border-radius:50%;background:var(--green)}
.brand__name{font-weight:600;font-size:16px;line-height:1.05;color:var(--green-deep);width:100px}
/* front */
.headline{position:absolute;right:28px;top:40px;text-align:right;color:var(--paper);text-transform:uppercase;line-height:1.15}
.headline .lg{font-size:25px;font-weight:800;display:block}
.headline .sm{font-size:17px;font-weight:400;display:block}
.pitch{position:absolute;left:34px;top:455px;width:410px;color:var(--paper)}
.pitch__lead{font-size:15px;font-weight:700;line-height:1.3;padding-bottom:8px;border-bottom:1px solid rgba(255,255,255,.8);width:300px}
.pitch__call{font-size:20px;font-weight:400;margin-top:8px}
.pitch__offer{font-size:34px;font-weight:600;line-height:1.05}
.front-footer{position:absolute;left:0;right:0;bottom:0;height:70px;background:rgba(255,255,255,.6);padding:14px 30px;font-size:14px;color:var(--ink-soft);line-height:1.35}
/* back */
.title{position:absolute;left:20px;top:118px;color:var(--paper);text-transform:uppercase;line-height:1}
.title .big{font-size:32px;font-weight:800;display:block}
.title .mid{font-size:19px;font-weight:600;display:block}
.intro{position:absolute;right:18px;top:24px;width:225px;font-size:8.4px;line-height:1.45;text-align:right;color:var(--ink)}
.intro p+p{margin-top:4px}
.badge{position:absolute;right:50px;top:232px;width:110px;height:32px;border-radius:6px;background:#e7eef7}
.help{position:absolute;right:18px;top:280px;width:200px}
.help__head{color:var(--green-text);font-weight:800;font-size:13px;text-transform:uppercase;text-align:center;line-height:1.2;margin-bottom:8px}
.help ul{list-style:none;font-size:8.8px;line-height:1.4;color:var(--ink)}
.help li{position:relative;padding-left:12px;margin-bottom:3px}
.help li::before{content:"";position:absolute;left:0;top:4px;width:5px;height:5px;border-radius:50%;background:var(--green-deep)}
.trained{position:absolute;left:20px;top:522px;width:240px;font-size:8.6px;line-height:1.45}
.contact__list{position:absolute;left:280px;top:524px;list-style:none;font-size:9px;line-height:1.6;color:var(--green-text);font-weight:600}
.contact__list li{display:flex;align-items:center;gap:5px}
.contact__list svg{width:9px;height:9px;fill:var(--ink-soft)}
.contact__label{position:absolute;left:22px;bottom:8px;color:var(--paper);font-size:26px;font-weight:800;letter-spacing:.5px}
</style>
</head>
<body>

<section class="flyer flyer--front" aria-label="Flyer front">
  <svg class="shapes" viewBox="0 0 480 680" aria-hidden="true">
    <defs>
      <linearGradient id="greyPhoto" x1="0" y1="0" x2="1" y2="1">
        <stop offset="0" stop-color="var(--photo-grey-b)"/>
        <stop offset=".5" stop-color="var(--photo-grey-a)"/>
        <stop offset="1" stop-color="var(--photo-grey-b)"/>
      </linearGradient>
    </defs>
    <rect width="480" height="680" fill="var(--green)"/>
    <path d="M0 0H230 C200 60 200 130 150 170 C100 210 50 230 0 260Z" fill="var(--paper)"/>
  </svg>
  <svg class="shapes" viewBox="0 0 480 680" role="img" aria-label="Black and white photo of a parent and baby sleeping cheek to cheek">
    <path d="M0 440 C80 330 200 330 290 390 C360 430 420 430 480 400V680H0Z" fill="url(#greyPhoto)"/>
    <path d="M150 370 C260 330 330 360 380 420" fill="none" stroke="var(--paper)" stroke-width="5"/>
  </svg>
  <div class="brand" style="left:26px;top:44px"><span class="brand__dot"></span><span class="brand__name">Hushwood Nestlings</span></div>
  <h1 class="headline">
    <span class="sm">We help</span>
    <span class="lg">Families &amp;</span>
    <span class="sm">their</span>
    <span class="lg">Little ones</span>
    <span class="sm">to get</span>
    <span class="lg">The sleep</span>
    <span class="sm">they need</span>
  </h1>
  <div class="pitch">
    <p class="pitch__lead">I can help with the sleep issues your child is experiencing</p>
    <p class="pitch__call">Call or email for a</p>
    <p class="pitch__offer">Free 15 minute consultation</p>
  </div>
  <p class="front-footer">I would love to connect with you to talk about your child's specific situation and discuss different solutions.</p>
</section>

<section class="flyer flyer--back" aria-label="Flyer back">
  <svg class="shapes" viewBox="0 0 480 680" aria-hidden="true">
    <defs>
      <linearGradient id="warmPhoto" x1="0" y1="0" x2="1" y2="1">
        <stop offset="0" stop-color="var(--photo-warm-b)"/>
        <stop offset=".45" stop-color="var(--photo-warm-a)"/>
        <stop offset="1" stop-color="#efe6e0"/>
      </linearGradient>
    </defs>
    <path d="M200 0H480V215 C400 215 300 220 250 180 C215 150 205 80 200 0Z" fill="var(--green)"/>
    <path d="M0 640 C150 610 320 625 480 590V680H0Z" fill="var(--green)"/>
  </svg>
  <svg class="shapes" viewBox="0 0 480 680" role="img" aria-label="Photo of a sleeping baby cuddled against a parent">
    <path d="M0 100 C80 100 160 150 205 190 C250 230 240 280 228 340 C214 410 218 470 226 500 H0Z" fill="url(#warmPhoto)"/>
    <path d="M236 200 C262 250 240 310 236 380 C233 440 238 480 252 500" fill="none" stroke="var(--green-deep)" stroke-width="4"/>
  </svg>
  <div class="brand" style="left:22px;top:24px"><span class="brand__dot"></span><span class="brand__name">Hushwood Nestlings</span></div>
  <h2 class="title">
    <span class="big">5 Steps</span>
    <span class="mid">to</span>
    <span class="big">Sleep</span>
    <span class="mid">through</span>
    <span class="big">the Night</span>
  </h2>
  <div class="intro">
    <p>If your baby or toddler isn't sleeping through the night, neither are you – and this means you are probably feeling physically and mentally exhausted, stressed, depressed and irritable, afraid you might be damaging your child and disconnected from your partner.</p>
    <p>The good news is nearly all healthy children 3 months or older are physically capable of sleeping 12 solid hours without waking. They just need to be taught the healthy sleep habits that enable them to do so.</p>
  </div>
  <div class="badge" role="img" aria-label="Certified consultant badge"></div>
  <div class="help">
    <p class="help__head">As a certified Dream Anchor™<br>I can help if:</p>
    <ul>
      <li>your child will only fall asleep when nursing or bottle feeding</li>
      <li>your child needs a dummy in order fall asleep</li>
      <li>you're waking up with your child one or more times per night</li>
      <li>your child needs to be rocked, patted, or taken for a car ride to go to sleep</li>
      <li>your own lack of sleep is starting to take a toll on your family</li>
    </ul>
  </div>
  <p class="trained">I've been personally trained by Marla Penwick, best selling author of <strong>The Dream Anchor™ Program</strong> to teach her sleep training methods to families like yours. Marla's methods have already helped over 30,000 parents and children and I'd be delighted to help your family next!</p>
  <ul class="contact__list">
    <li><svg viewBox="0 0 10 10"><path d="M2 0h2l1 3-1.5 1a6 6 0 0 0 2.5 2.5L7 5l3 1v2c0 1-1 2-2 2A8 8 0 0 1 0 2c0-1 1-2 2-2z"/></svg>0491 570 156</li>
    <li><svg viewBox="0 0 10 10"><rect width="10" height="10" rx="2"/></svg>hushwoodnestlings</li>
    <li><svg viewBox="0 0 10 10"><circle cx="5" cy="5" r="5"/></svg>hushwoodnestlings.com.au</li>
    <li><svg viewBox="0 0 10 10"><path d="M0 2h10v6H0z"/></svg>june@hushwoodnestlings.com.au</li>
  </ul>
  <p class="contact__label">CONTACT US</p>
</section>

</body>
</html>
```